Chocolate company needing sticker for products

I have a small chocolate company Willow Bend Sweets in Austin Texas. I make all vegan, gluten free, organic, faire trade chocolate that tastes amazing! It is allergy friendly approvable by all ages. I want to have a great sticker that i can put on our boxes and bags. I am using a lot of natural craft color and brown. I am open to color options possibly for different flavors. I want the packaging to reflect the basis of my company. It is all handmade by me but i don't want it to have to much of a crafty look to it. I have attached the logo designs I have. it the sticker can have som of the bullet points about the company that would be great. But it needs to say Locally Made in Austin Texas. it also has to have the company address.
418 West Cobbler Ridge Rd #207 Austin Tx 78745. These things are required by the state for food regulations. I want something that looks great and I can be really proud to put on my product! Thanks so much for all of your help in advance. Dot

I also need some other information added to the sticker. Website which is willowbendsweetsatx.com 

Phone number 512.368.4175. Instagram willowbendsweets. Thanks for your hard work! 

Industry/Entity Type

Chocolate Company

Requirements
Must have
• The logo is added at the bottom as well as designs I like I want to have a professional look but it to be approvable by all consumers. I will gig feed back as i see what designs come through. This will probably fold out into a multi design project so i will be looking for assistance on other areas of this as well. Thanks

```html
<!DOCTYPE html>
<html lang="en">
<head>
<meta charset="utf-8">
<title>Moonberry Bites Sticker – Willow Bend Sweets</title>
<link rel="stylesheet" href="https://fonts.googleapis.com/css2?family=IM+Fell+English&family=Marcellus+SC&family=Tenor+Sans&display=swap">
<style>
  :root {
    --page: #ffffff;
    --sky: #acdae1;
    --sky-line: #9ccbd3;
    --cocoa: #401d05;
    --cream: #ffffff;
    --dot: #acdae1;
  }
  * { margin: 0; padding: 0; box-sizing: border-box; }
  html, body {
    width: 1200px; height: 1000px; overflow: hidden;
    background: var(--page);
  }
  .canvas { position: relative; width: 1200px; height: 1000px; }
  .sticker {
    position: absolute; left: 235px; top: 0;
    width: 728px; height: 1000px;
    background: var(--sky);
  }
  .fold-line {
    position: absolute; left: 0; right: 0; top: 498px;
    height: 2px; background: var(--sky-line);
  }
  .label {
    position: absolute; left: 48px; top: 46px;
    width: 635px; height: 394px;
    background: var(--cocoa); color: var(--cream);
    text-align: center;
    font-family: "Tenor Sans", sans-serif;
  }
  .product-name {
    position: absolute; left: 0; right: 0; top: 34px;
    font-family: "IM Fell English", Georgia, serif;
    font-size: 74px; line-height: 1; letter-spacing: 2px;
    font-weight: 400;
  }
  .flavor {
    position: absolute; left: 0; right: 0; top: 132px;
    font-family: "IM Fell English", Georgia, serif;
    font-size: 22px; line-height: 36px; letter-spacing: 1.5px;
    text-transform: uppercase;
  }
  .divider {
    position: absolute; left: 22px; right: 22px; top: 228px;
    height: 4px;
    background-image: radial-gradient(circle, var(--dot) 1.6px, transparent 1.8px);
    background-size: 6px 4px;
  }
  .origin {
    position: absolute; left: 0; right: 0; top: 250px;
    font-family: "Marcellus SC", "Tenor Sans", sans-serif;
    font-size: 31px; letter-spacing: 0.5px;
  }
  .claim {
    position: absolute; line-height: 1;
    font-family: "Tenor Sans", sans-serif;
    font-size: 20px; letter-spacing: 0.5px;
  }
  .ornament {
    position: absolute; top: 332px; width: 14px; height: 30px;
    background: var(--cream);
    clip-path: polygon(50% 0, 100% 50%, 50% 100%, 0 50%);
  }
  .brand {
    position: absolute; left: 0; right: 0; top: 600px;
    text-align: center; color: var(--cocoa);
    font-family: "Marcellus SC", "Tenor Sans", sans-serif;
    font-size: 50px; line-height: 62px; letter-spacing: 1px;
  }
  .ingredients {
    position: absolute; left: 48px; width: 635px; top: 860px;
    color: var(--cocoa);
    font-family: "Tenor Sans", sans-serif;
    font-size: 15px; line-height: 27px; letter-spacing: 0.4px;
    text-transform: uppercase; text-align: justify;
    text-align-last: left;
  }
  .address {
    position: absolute; left: 0; right: 0; top: 930px;
    text-align: center; color: var(--cocoa);
    font-family: "Marcellus SC", "Tenor Sans", sans-serif;
    font-size: 26px; letter-spacing: 0.8px; white-space: nowrap;
  }
</style>
</head>
<body>
<main class="canvas">
  <section class="sticker">
    <div class="fold-line"></div>

    <div class="label">
      <h1 class="product-name">Moonberry Bites</h1>
      <p class="flavor">Creamy mulberry-infused<br>70% dark chocolate</p>
      <div class="divider"></div>
      <p class="origin">Locally Made in Austin, Texas</p>

      <span class="claim" style="left:21px; top:312px;">VEGAN</span>
      <span class="claim" style="left:21px; top:352px;">GLUTEN FREE</span>
      <span class="ornament" role="img" aria-label="small decorative ornament" style="left:199px;"></span>
      <span class="claim" style="left:276px; top:312px;">ORGANIC</span>
      <span class="claim" style="left:250px; top:352px;">ALLERGY FREE</span>
      <span class="ornament" role="img" aria-label="small decorative ornament" style="left:436px;"></span>
      <span class="claim" style="right:21px; top:320px;">FAIR TRADE</span>
      <span class="claim" style="right:21px; top:355px;">DELICIOUS</span>
    </div>

    <p class="brand">Willow Bend<br>Sweets</p>

    <p class="ingredients">Ingredients: cacao, coconut milk, rice milk, mulberry, vanillin, mulberry extract, salt, coloring.</p>

    <p class="address">418 West Cobbler Ridge Rd #207 Austin Tx 78745</p>
  </section>
</main>
</body>
</html>
```